Tallwick Haven National Website

We need a website to match our Logo. We will be selling american made vapeing Oils, batteries, Cartomizers, Clearomizers. We have a wharehouse location with couches, TVs streaming clipora, vending machine, and the worlds first flavor mixing bar. We have the lowest priced high grade oils. We will send pictures of the location. Relaxed atmoshpere and no lines for purchase. VIP cards for regulars.

(PLEASE KNOW THAT THE LOGO IS THE UPPER RIGHT LOGO ONLY OF THE FOUR ON THE FILE I ATTACHED)
Updates

Keep in mind we are are only looking for concept and a non coded website

Please know that we are looking for a non coded website

Industry/Entity Type

Purchase

Requirements
Must have
• Online cart, Blog,

```html
<!DOCTYPE html>
<html lang="en">
<head>
<meta charset="utf-8">
<title>Tallwick Haven National</title>
<link href="https://fonts.googleapis.com/css2?family=Arimo:wght@400;700&family=Roboto+Condensed:wght@300;400&display=swap" rel="stylesheet">
<style>
:root{
  --dark:#34352f;
  --green:#8dc63f;
  --green-dark:#6fa52a;
  --green-text:#9cc84a;
  --ink:#222;
  --grey-bg:#ececec;
  --light:#f7f7f7;
  --box-dark:#2a3514;
  --black:#000;
}
*{margin:0;padding:0;box-sizing:border-box}
html,body{width:1166px;height:1200px;overflow:hidden}
body{font-family:"Arimo",Arial,sans-serif;color:var(--ink);background:var(--light);position:relative}
.abs{position:absolute}
.header{left:0;top:0;width:1166px;height:117px;background:radial-gradient(ellipse at 55% 40%,#6a6b64 0%,var(--dark) 55%)}
.brand{left:194px;top:28px;font-size:40px;color:var(--green);font-weight:400;letter-spacing:-1px}
.brand-mark{left:194px;top:22px;width:8px;height:8px;background:var(--green)}
.cart{left:710px;top:28px;color:#fff;font-family:"Roboto Condensed",sans-serif;font-size:12px;line-height:24px}
.cart svg{vertical-align:-3px;margin-right:4px}
.cart .count{padding-left:18px}
.contact-pills{left:832px;top:24px}
.pill{width:129px;height:15px;border-radius:7px;background:#9a9b95;color:#3a3b36;font-size:10.5px;line-height:15px;padding-left:12px;margin-bottom:3px}
.page-band{left:0;top:117px;width:1166px;height:371px;background:radial-gradient(ellipse at 40% 50%,#fff 0%,#f2f2f2 50%,#e6e6e6 100%)}
.nav{left:170px;top:95px;width:830px;height:41px;border-radius:6px;background:linear-gradient(#e6f5c8,#a6d65c);display:flex;align-items:center;box-shadow:0 3px 5px rgba(0,0,0,.15)}
.nav a{font-family:"Roboto Condensed",sans-serif;font-size:12px;color:#222;text-decoration:none;padding:0 15px 0 25px;height:41px;line-height:41px;border-right:1px solid #b8d98a}
.nav a:last-of-type{border-right:none}
.search{left:705px;top:105px;width:266px;height:21px;background:#e4e4e4;font-size:11px;color:#888;line-height:21px;padding-left:10px}
.search-btn{left:953px;top:105px;width:18px;height:21px;background:#333}
.hero-title{left:207px;top:186px;font-size:21px;font-weight:700;color:#222}
.product-img{left:203px;top:256px;width:230px;height:110px;background:linear-gradient(135deg,#3a3a3a,#8c1d1d 50%,#e8e8e8);border-radius:6px}
.swoosh{left:194px;top:371px;width:451px;height:110px;background:radial-gradient(ellipse at 50% 60%,#cfe59e 0%,rgba(230,230,230,0) 70%)}
.hero-list{left:468px;top:224px;color:var(--green-text);font-weight:700;font-size:15px;line-height:24px;list-style:none}
.btn{background:linear-gradient(#9fd357,var(--green-dark));color:#fff;font-weight:700;font-size:15.5px;border-radius:3px;text-align:center;box-shadow:0 2px 0 #5c8a22;border:1px solid #7bb33a}
.btn.grey{background:linear-gradient(#dedede,#b5b5b5);color:#777;box-shadow:0 2px 0 #888;border:1px solid #ccc}
.quote-tab{left:696px;top:201px;width:269px;height:46px;border-radius:8px 8px 0 0;background:linear-gradient(#f2f2f2,#dcdcdc);font-size:19px;color:#333;padding:12px 0 0 15px}
.quote-box{left:678px;top:241px;width:309px;height:198px;border-radius:8px;background:#e2e2e2;border:1px solid #d4d4d4}
.quote-text{left:705px;top:249px;width:270px;font-size:10.5px;line-height:14px;color:#333}
.field{background:#fff;border:1px solid #d0d0d0;font-size:10.5px;color:#888;padding-left:9px;line-height:30px;height:32px}
.help{left:801px;top:371px;width:168px;height:39px;border-radius:3px;background:linear-gradient(#fff,#e6e6e6);border:1px solid #bbb;box-shadow:0 2px 0 #999;font-size:10.5px;color:#333;padding:4px 0 0 47px;line-height:14px}
.help svg{position:absolute;left:10px;top:6px}
.green-band{left:0;top:488px;width:1166px;height:243px;background:var(--green)}
.cond{font-family:"Roboto Condensed",sans-serif;font-weight:300}
.welcome-h{left:187px;top:514px;color:#fff;font-size:22px}
.welcome-lead{left:187px;top:553px;width:400px;color:#fff;font-weight:700;font-size:13.5px;line-height:17px}
.welcome-body{left:187px;top:612px;width:500px;color:#fff;font-size:10.5px;line-height:14px}
.services-h{left:720px;top:511px;color:#fff;font-size:22px}
.service{left:720px;width:237px;background:var(--box-dark);color:#fff;font-size:10.5px;line-height:13px;padding:6px 10px;border-radius:2px}
.section-h{font-family:"Roboto Condensed",sans-serif;font-size:20px;color:#333;top:758px}
.photo{top:795px;width:223px;height:90px}
.col-text{font-size:10.5px;line-height:14px;color:#222}
.bullets{list-style:none}
.bullets li{position:relative;padding-left:14px}
.bullets li::before{content:"";position:absolute;left:0;top:3px;border-left:6px solid var(--green);border-top:4px solid transparent;border-bottom:4px solid transparent}
.newsletter{left:710px;top:1038px;width:270px;height:32px;background:#fff;border:1px solid #ccc}
.news-btn{left:971px;top:1043px;width:17px;height:21px;background:#333}
.footer{left:0;top:1096px;width:1166px;height:104px;background:var(--black)}
.foot-nav{left:185px;top:1113px;color:#fff;font-family:"Roboto Condensed",sans-serif;font-size:12px;word-spacing:2px}
.foot-nav span{margin:0 10px;color:#aaa}
.copy{left:185px;top:1137px;color:#999;font-size:10.5px}
.copy b{font-weight:400;color:#fff;margin-left:12px}
.cards{left:714px;top:1114px;display:flex;gap:3px}
.card{width:37px;height:24px;border-radius:2px;border:1px solid #fff}
</style>
</head>
<body>
<div class="abs header"></div>
<div class="abs page-band"></div>
<div class="abs brand-mark"></div>
<div class="abs brand">Tallwick Haven</div>
<div class="abs cart">
  <svg width="14" height="18" viewBox="0 0 14 18"><rect x="1" y="5" width="12" height="12" rx="1" fill="#f2b01e"/><path d="M4 6V3a3 3 0 0 1 6 0v3" stroke="#fff" fill="none" stroke-width="1.5"/></svg>SHOPING<br><span class="count">CART : 00</span>
</div>
<div class="abs contact-pills">
  <div class="pill">+1 555 014 2287</div>
  <div class="pill">+1 555 014 2287</div>
  <div class="pill">hello@tallwickhaven.com</div>
</div>

<nav class="abs nav">
  <a href="#">HOME</a><a href="#">ABOUT US</a><a href="#">SERVICES</a><a href="#">PRODUCTS</a><a href="#">BLOG</a><a href="#">CONTACT US</a>
</nav>
<div class="abs search">Search here...</div>
<div class="abs search-btn"><svg width="18" height="21" viewBox="0 0 18 21"><path d="M7 6l4 4.5L7 15" stroke="#fff" fill="none" stroke-width="1.5"/></svg></div>

<h1 class="abs hero-title">WE WILL BE SELLING AMERICAN MADE</h1>
<div class="abs product-img" role="img" aria-label="Three vape batteries product photo"></div>
<div class="abs swoosh" role="img" aria-label="Green swirl decoration"></div>
<ul class="abs hero-list"><li>VAPEING OILS,</li><li>BATTERIES,</li><li>CARTOMIZERS,</li><li>CLEAROMIZERS.</li></ul>
<div class="abs btn" style="left:467px;top:336px;width:109px;height:34px;line-height:32px">Learn More</div>

<div class="abs quote-box"></div>
<div class="abs quote-tab">FOR A FREE <b>QUOTE</b></div>
<p class="abs quote-text">Morbi nunc odio, gravida at, cursus nec, luctus a, lorem. Maecenas tristique orci ac sem. Duis ultricies</p>
<div class="abs field" style="left:698px;top:290px;width:270px">* Your name ...</div>
<div class="abs field" style="left:698px;top:325px;width:170px">* Telephone ...</div>
<div class="abs field" style="left:873px;top:325px;width:95px">Zip code</div>
<div class="abs btn" style="left:698px;top:371px;width:91px;height:39px;line-height:37px;font-size:21px">Send</div>
<div class="abs help">
  <svg width="30" height="26" viewBox="0 0 30 26"><path d="M4 18V13a11 11 0 0 1 22 0v5" stroke="#222" stroke-width="2.5" fill="none"/><rect x="2" y="15" width="5" height="9" rx="2" fill="#222"/><rect x="23" y="15" width="5" height="9" rx="2" fill="#222"/></svg>
  Live Logistics Help at<br><b style="font-size:12px">+1 555 019 3380</b>
</div>

<div class="abs green-band"></div>
<h2 class="abs welcome-h cond">Welcome to our Company</h2>
<p class="abs welcome-lead">Tallwick Haven National &nbsp; ursus nec luctus a lorem. Maecenas tristique orci ac sem. Duis ultricies PHARETRA MAGNA. Donec accumsan malesuada orci.</p>
<p class="abs welcome-body">Morbi nunc odio, gravida at, cursus nec, luctus a, lorem. Maecenas tristique orci ac sem. Duis ultricies pharetra magna. Donec accumsan malesuada orci. Donec sit amet eros. Lorem ipsum dolor sit amet, consectetuer adipiscing elit. Mauris fermentum dictum magna. Sed laoreet aliquam leo. Ut tellus dolor, dapibus eget, elementum vel, cursus eleifend, elit. Aenean auctor wisi et urna. Aliquam erat volutpat. Duis ac turpis. Integer rutrum ante eu lacus.</p>
<h2 class="abs services-h cond">Our Services</h2>
<div class="abs service" style="top:545px">Duis ultricies pharetra magna. Donec accum san malesuada orci.</div>
<div class="abs service" style="top:583px;background:#000">Sit amet eros. Lorem ipsum dolor sit amet, consectetuer adipiscing elit.</div>
<div class="abs service" style="top:621px">Donec sit amet eros.</div>
<div class="abs btn grey" style="left:722px;top:657px;width:108px;height:34px;line-height:32px">Learn More</div>

<h2 class="abs section-h" style="left:188px">ABOUT US</h2>
<h2 class="abs section-h" style="left:449px">OUR PRODUCTS</h2>
<h2 class="abs section-h" style="left:715px">TESTIMONIALS</h2>
<div class="abs photo" style="left:185px;background:linear-gradient(90deg,#4d8fcf,#d9eaf7 60%,#2b2b2b)" role="img" aria-label="Customer service representative on the phone"></div>
<div class="abs photo" style="left:449px;background:linear-gradient(135deg,#7a3a1a,#e6d9c4 50%,#b6532a)" role="img" aria-label="Lounge bed with pillows"></div>
<p class="abs col-text" style="left:186px;top:900px;width:225px">Morbi nunc odio, gravida at, cursus nec, luctus a, lorem. Maecenas tristique orci ac sem. Duis ultricies pharetra magna. Donec accumsan malesuada orci. Donec sit amet eros. Lorem ipsum dolor sit amet,<br><br>consectetuer adipiscing elit. Mauris fermentum dictum magna. Sed laoreet aliquam leo.</p>
<ul class="abs col-text bullets" style="left:460px;top:900px;width:140px">
  <li>Morbi nunc odio, gravida</li><li>at, cursus nec, luctus a,</li><li>lorem. Maecenas</li><li>tristique orci ac sem.</li><li>Duis ultricies pharetra</li><li>magna. Donec</li><li>accumsan</li>
</ul>
<p class="abs col-text" style="left:720px;top:794px;width:265px">Morbi nunc odio, gravida at, cursus nec, luctus a, lorem. Maecenas tristique orci ac sem. Duis ultricies Donec sit amet eros. Lorem ipsum dolor sit amet,<br><br>consectetuer adipiscing elit. Mauris fermentum dictum magna. Sed laoreet aliquam leo.<br><br><b style="color:#000">Name<br>USA</b></p>
<div class="abs btn" style="left:717px;top:926px;width:109px;height:34px;line-height:32px">Learn More</div>
<div class="abs btn" style="left:185px;top:1038px;width:109px;height:34px;line-height:32px">Learn More</div>
<div class="abs btn" style="left:449px;top:1036px;width:109px;height:34px;line-height:32px">Learn More</div>
<h2 class="abs section-h" style="left:715px;top:991px">NEWSLETTER</h2>
<div class="abs newsletter"></div>
<div class="abs news-btn"><svg width="17" height="21" viewBox="0 0 17 21"><path d="M6 6l4 4.5L6 15" stroke="#fff" fill="none" stroke-width="1.5"/></svg></div>

<footer class="abs footer"></footer>
<div class="abs foot-nav">HOME<span>|</span>ABOUT US<span>|</span>SERVICES<span>|</span>PRODUCTS<span>|</span>BLOG<span>|</span>CONTACT US</div>
<div class="abs copy">Tallwick Haven Ntional &nbsp;© 2013 &nbsp;&nbsp; | <b>Privacy Policy</b></div>
<div class="abs cards">
  <div class="card" style="background:#2a3a8c"></div>
  <div class="card" style="background:#e0432a"></div>
  <div class="card" style="width:24px;background:#3a8fd0"></div>
  <div class="card" style="width:33px;background:#6d6d5a"></div>
</div>
</body>
</html>
```